Multiple projects tracking on one dashboard with excel data

I am a project manager and my team have multiple projects to handle. Projects comprises of different customer with different project creation/allocation dates, start and completion dates.

This dashboard shall be able to showcase the number of ongoing projects, project overdue/delayed.

In sample data attached, there are multiple projects (customer sites), there can be one system used at one project site or multiple type of systems use at same site.

Important details for calculation and shown in dashboard as such:
1) Number of ongoing projects
2) Number of projects delayed
3) Numbers of projects cancelled
4) Number of projects completed within 6 months/1 year (It will be good if dashboard perimeter can be changed to 3 months or any other variants). This shall be Project start day minus Project End date)
5) Number of on-going projects - days calculated till date, from project start date. Rank of the project that is taking most days and months.
6) Days between job creation date and project start date.
7) Engineers who took lesser time to start a project (project start date - job creation date)
6) Number of projects per engineer
7) Engineers ranking on days took to complete a project.
8) Total project value.
9) Individual engineer project value

Any other not shown in sample data but good to have
1) by input of project completion forecast date in a field, project value forecast can be calculated.

Other good suggestion can be provided and i will up the payment
Additional feature if this data and dashboard can be simple use on iphone for presentation.

```html
<!DOCTYPE html>
<html lang="en">
<head>
<meta charset="utf-8">
<title>Project Tracking Dashboard</title>
<link rel="stylesheet" href="https://fonts.googleapis.com/css2?family=Open+Sans:wght@400;600&family=Barlow:wght@400;500&display=swap">
<style>
:root{
  --canvas:#ffffff;
  --tile-border:#e3e3e3;
  --title:#252423;
  --value:#252423;
  --bar:#118dff;
  --axis-text:#605e5c;
  --label-dark:#252423;
  --label-light:#ffffff;
  --check-border:#9b9b9b;
}
*{box-sizing:border-box;margin:0;padding:0}
html,body{width:1200px;height:653px;overflow:hidden;background:var(--canvas)}
body{position:relative;font-family:"Open Sans",Arial,sans-serif;color:var(--title)}
.tile{position:absolute;border:1px solid var(--tile-border);background:var(--canvas)}
.tile-title{position:absolute;left:8px;top:4px;font-size:14px;font-weight:400;color:var(--title);white-space:nowrap}
.kpi-value{position:absolute;left:0;right:0;top:44px;text-align:center;font-family:"Barlow",Arial,sans-serif;font-size:48px;font-weight:500;color:var(--value);letter-spacing:.5px}
.chart{position:absolute;left:0;top:0}
.chart text{font-family:"Open Sans",Arial,sans-serif}
.axis{font-size:11px;fill:var(--axis-text)}
.cat{font-size:11px;fill:var(--axis-text)}
.val{font-size:11px;fill:var(--label-dark)}
.val-in{font-size:11px;fill:var(--label-light);font-weight:600}
.bar{fill:var(--bar)}
.filter-option{position:absolute;left:14px;top:28px;display:flex;align-items:center;gap:6px;font-size:12px;color:var(--axis-text)}
.checkbox{width:11px;height:11px;border:1px solid var(--check-border);background:var(--canvas)}

.avg-start-card{left:8px;top:5px;width:274px;height:120px}
.total-card{left:309px;top:5px;width:196px;height:120px}
.delayed-card{left:505px;top:5px;width:197px;height:120px}
.cancelled-card{left:702px;top:5px;width:195px;height:120px}
.value-card{left:920px;top:5px;width:274px;height:120px}
.per-engineer{left:309px;top:125px;width:588px;height:210px}
.value-by-engineer{left:920px;top:125px;width:274px;height:210px}
.filter-panel{left:8px;top:250px;width:282px;height:85px}
.by-completion{left:8px;top:347px;width:282px;height:300px}
.avg-start-chart{left:309px;top:347px;width:292px;height:300px}
.completion-time-chart{left:612px;top:347px;width:285px;height:300px}
.completion-days{left:920px;top:347px;width:274px;height:300px}
</style>
</head>
<body>

<section class="tile avg-start-card">
  <h2 class="tile-title">Average # of Days to Start a Project</h2>
  <p class="kpi-value">62.78</p>
</section>

<section class="tile total-card">
  <h2 class="tile-title">Total # of Projects</h2>
  <p class="kpi-value">9</p>
</section>

<section class="tile delayed-card">
  <h2 class="tile-title"># of Delayed Projects</h2>
  <p class="kpi-value">0</p>
</section>

<section class="tile cancelled-card">
  <h2 class="tile-title"># of Cancelled Projects</h2>
  <p class="kpi-value">2</p>
</section>

<section class="tile value-card">
  <h2 class="tile-title">Total Project Value</h2>
  <p class="kpi-value">1,499,999</p>
</section>

<section class="tile per-engineer">
  <h2 class="tile-title"># of Project per Engineer</h2>
  <svg class="chart" width="588" height="210" viewBox="0 0 588 210">
    <text class="axis" x="6" y="35">4</text>
    <text class="axis" x="6" y="73">3</text>
    <text class="axis" x="6" y="110">2</text>
    <text class="axis" x="6" y="148">1</text>
    <text class="axis" x="6" y="185">0</text>
    <rect class="bar" x="69" y="31" width="94" height="150"/>
    <rect class="bar" x="193" y="68.5" width="93" height="112.5"/>
    <rect class="bar" x="314" y="143.5" width="94" height="37.5"/>
    <rect class="bar" x="437" y="143.5" width="93" height="37.5"/>
    <text class="val-in" x="116" y="47" text-anchor="middle">4</text>
    <text class="val" x="239.5" y="63" text-anchor="middle">3</text>
    <text class="val" x="361" y="138" text-anchor="middle">1</text>
    <text class="val" x="483.5" y="138" text-anchor="middle">1</text>
    <text class="cat" x="116" y="197" text-anchor="middle">Jerry</text>
    <text class="cat" x="239.5" y="197" text-anchor="middle">John</text>
    <text class="cat" x="361" y="197" text-anchor="middle">Lionel</text>
    <text class="cat" x="483.5" y="197" text-anchor="middle">Tom</text>
  </svg>
</section>

<section class="tile value-by-engineer">
  <h2 class="tile-title">Total Project Value</h2>
  <svg class="chart" width="274" height="210" viewBox="0 0 274 210">
    <text class="cat" x="14" y="63">Jerry</text>
    <text class="cat" x="14" y="103">John</text>
    <text class="cat" x="14" y="142">Tom</text>
    <text class="cat" x="14" y="178">Lionel</text>
    <rect class="bar" x="46" y="45" width="224" height="29"/>
    <rect class="bar" x="46" y="85" width="56" height="29"/>
    <rect class="bar" x="46" y="124" width="45" height="28"/>
    <rect class="bar" x="46" y="160" width="11" height="29"/>
    <text class="val-in" x="265" y="63" text-anchor="end">1,000,000</text>
    <text class="val" x="106" y="103">249,999</text>
    <text class="val" x="95" y="142">200,000</text>
    <text class="val" x="61" y="178">50,000</text>
  </svg>
</section>

<section class="tile filter-panel">
  <h2 class="tile-title">Filter</h2>
  <label class="filter-option"><span class="checkbox"></span>Within 6 Months</label>
</section>

<section class="tile by-completion">
  <h2 class="tile-title"># of Projects by Completion Time</h2>
  <svg class="chart" width="282" height="300" viewBox="0 0 282 300">
    <text class="val" x="138.5" y="48" text-anchor="middle">9</text>
    <rect class="bar" x="110" y="55" width="57" height="208"/>
    <text class="cat" x="138.5" y="276" text-anchor="middle">Within 6</text>
    <text class="cat" x="138.5" y="290" text-anchor="middle">Months</text>
  </svg>
</section>

<section class="tile avg-start-chart">
  <h2 class="tile-title">Average # of Days to Start a Project</h2>
  <svg class="chart" width="292" height="300" viewBox="0 0 292 300">
    <text class="cat" x="14" y="76">Jerry</text>
    <text class="cat" x="14" y="128">Tom</text>
    <text class="cat" x="14" y="180">John</text>
    <text class="cat" x="14" y="234">Lionel</text>
    <rect class="bar" x="47" y="53" width="153" height="39"/>
    <rect class="bar" x="47" y="105" width="64" height="39"/>
    <rect class="bar" x="47" y="157" width="56" height="39"/>
    <rect class="bar" x="47" y="210" width="3" height="40"/>
    <text class="val" x="206" y="76">102</text>
    <text class="val" x="117" y="128">43</text>
    <text class="val" x="109" y="180">37</text>
    <text class="val" x="56" y="234">2</text>
    <text class="axis" x="47" y="287" text-anchor="middle">0</text>
    <text class="axis" x="198" y="287" text-anchor="middle">100</text>
  </svg>
</section>

<section class="tile completion-time-chart">
  <h2 class="tile-title"># of Project by Completion Time</h2>
  <svg class="chart" width="285" height="300" viewBox="0 0 285 300">
    <text class="axis" x="0" y="0" transform="translate(20 136) rotate(-90)" text-anchor="middle">Completion Time</text>
    <text class="axis" x="40" y="112" text-anchor="end">10</text>
    <text class="axis" x="40" y="183" text-anchor="end">5</text>
    <text class="axis" x="40" y="253" text-anchor="end">0</text>
    <rect class="bar" x="48" y="37" width="230" height="47"/>
    <rect class="bar" x="48" y="219" width="115" height="31"/>
    <text class="val-in" x="272" y="65" text-anchor="end">2</text>
    <text class="val" x="169" y="239">1</text>
    <text class="axis" x="48" y="287" text-anchor="middle">0</text>
    <text class="axis" x="163" y="287" text-anchor="middle">1</text>
    <text class="axis" x="276" y="287" text-anchor="middle">2</text>
  </svg>
</section>

<section class="tile completion-days">
  <h2 class="tile-title">Completion Days by Engineer</h2>
  <svg class="chart" width="274" height="300" viewBox="0 0 274 300">
    <text class="cat" x="14" y="155">John</text>
    <rect class="bar" x="40" y="126" width="170" height="50"/>
    <text class="val-in" x="204" y="155" text-anchor="end">28</text>
    <text class="axis" x="40" y="287" text-anchor="middle">0</text>
    <text class="axis" x="161" y="287" text-anchor="middle">20</text>
  </svg>
</section>

</body>
</html>
```